Name Card Design

Looking to create a card for my business. I am a personal stylist, my business is clothes, shoes and everything to do with looking fashion forward. I help people achieve the most polished look with cloths and grooming. I would like my card to be a reflection of my qualities which are: poise, elegance, creativity and fairness.
Things I like a simple yet expensive looking, sometimes less simple but highly creative and different catches my eye. For instance I saw a card with lace trimming at the bottom, it made me think about the business that person was in. I don't like childish designs with butterflies, trees, flowers, etc.
Here is my site www.Marta-Venn.example for your perusal

On the card it should have the following info
Marta Venn
personal stylist
www.Marta-Venn.example
(+65) 842-30587
Facebook page: Ringtochic

Back of the card:
Wardrobe weeding
Personal shopping
Style consultation

Target Market(s)

mostly working women

Industry/Entity Type

Fashion

Font styles to use
Serif
Sans Serif

Requirements
Should not have
• butterflies, flowers, feathers, etc

```html
<!DOCTYPE html>
<html lang="en">
<head>
<meta charset="utf-8">
<title>Marta Venn – Personal Stylist Business Card</title>
<link rel="stylesheet" href="https://fonts.googleapis.com/css2?family=Inter:wght@300;400;700&display=swap">
<style>
  :root {
    --canvas: #ececec;
    --card: #ffffff;
    --ink: #111111;
    --band: #0a0a0a;
    --band-text: #ffffff;
    --bullet-ring: #cfe3e6;
  }
  html, body {
    margin: 0;
    padding: 0;
    width: 1200px;
    height: 1000px;
    overflow: hidden;
    background: var(--canvas);
    font-family: "Inter", "Helvetica Neue", Arial, sans-serif;
    color: var(--ink);
  }
  .stage {
    position: relative;
    width: 1200px;
    height: 1000px;
  }
  .card {
    position: absolute;
    top: 57px;
    width: 529px;
    height: 293px;
    background: var(--card);
  }
  .card--front { left: 67px; }
  .card--back { left: 637px; }

  .identity {
    position: absolute;
    right: 16px;
    top: 28px;
    text-align: right;
  }
  .identity__name {
    margin: 0;
    font-weight: 700;
    font-size: 33px;
    line-height: 36px;
    letter-spacing: -0.2px;
  }
  .identity__role {
    margin: 0;
    font-weight: 300;
    font-size: 22px;
    line-height: 22px;
    letter-spacing: -0.3px;
  }

  .web-band {
    position: absolute;
    left: 5px;
    top: 129px;
    width: 278px;
    height: 59px;
    background: var(--band);
    color: var(--band-text);
    font-weight: 300;
    font-size: 20px;
    line-height: 59px;
    text-align: center;
    letter-spacing: -0.2px;
  }
  .web-band__shadow {
    position: absolute;
    left: 150px;
    top: 180px;
    width: 210px;
    height: 20px;
  }

  .contact {
    position: absolute;
    right: 16px;
    top: 223px;
    text-align: right;
    font-weight: 300;
    font-size: 22px;
    line-height: 30px;
    letter-spacing: -0.3px;
  }
  .contact__line { margin: 0; }
  .contact__social {
    display: inline-flex;
    align-items: center;
    gap: 4px;
  }
  .contact__dot {
    width: 20px;
    height: 20px;
    border-radius: 50%;
    background: var(--ink);
    box-shadow: 0 0 0 2px var(--bullet-ring);
  }

  .services {
    position: absolute;
    right: 16px;
    top: 80px;
    margin: 0;
    padding: 0;
    list-style: none;
    text-align: right;
  }
  .services__item {
    display: flex;
    align-items: center;
    justify-content: flex-end;
    height: 60px;
    font-weight: 300;
    font-size: 18px;
    letter-spacing: 4.4px;
    text-transform: uppercase;
  }
  .services__bullet {
    width: 10px;
    height: 10px;
    border-radius: 50%;
    background: var(--ink);
    box-shadow: 0 0 0 2px var(--bullet-ring);
    margin-right: 32px;
  }
  .services__item:nth-child(2) .services__bullet { margin-right: 28px; }
  .services__item:nth-child(3) .services__bullet { margin-right: 22px; }
</style>
</head>
<body>
<main class="stage">
  <section class="card card--front" aria-label="Card front">
    <div class="identity">
      <h1 class="identity__name">Marta Venn</h1>
      <p class="identity__role">personal stylist</p>
    </div>

    <svg class="web-band__shadow" viewBox="0 0 210 20" aria-hidden="true">
      <defs>
        <radialGradient id="bandShade" cx="0.45" cy="0.3" r="0.55">
          <stop offset="0" stop-color="#000" stop-opacity="0.55"/>
          <stop offset="1" stop-color="#000" stop-opacity="0"/>
        </radialGradient>
      </defs>
      <ellipse cx="100" cy="8" rx="110" ry="10" fill="url(#bandShade)"/>
    </svg>
    <div class="web-band">www.Marta-Venn.example</div>

    <div class="contact">
      <p class="contact__line">F . + 65 842 30587</p>
      <p class="contact__line"><span class="contact__social"><span class="contact__dot"></span>Ringtochic</span></p>
    </div>
  </section>

  <section class="card card--back" aria-label="Card back">
    <ul class="services">
      <li class="services__item"><span class="services__bullet"></span>Wardrobe weeding</li>
      <li class="services__item"><span class="services__bullet"></span>Personal shopping</li>
      <li class="services__item"><span class="services__bullet"></span>Style consultation</li>
    </ul>
  </section>
</main>
</body>
</html>
```